business card for a shoe shop

we would like a business card for a family owned shoe shop.
With this information included.
Darnell's Shoe Store
Family owned since 1947

then on other side
Darnell's Shoe Store
Footwear fitting specialist
Phone: 9187 2630
218 Quarry St, Fernleigh Downs 3187
(cnr. Hartwick Rd and Quarry St)
darnellshoes218@examplemail.com
if could incorporate the purple color on card i have attached.

```html
<!DOCTYPE html>
<html lang="en">
<head>
<meta charset="utf-8">
<title>Darnell's Shoe Store – Business Card</title>
<link rel="stylesheet" href="https://fonts.googleapis.com/css2?family=Cormorant+Garamond:wght@600&family=Quicksand:wght@500&display=swap">
<style>
  :root {
    --lilac-bg: #e6dbed;
    --card-purple: #9f84bd;
    --ink-purple: #7a5ba3;
    --icon-purple: #9275b6;
    --card-white: #f4f3f5;
    --rule-light: #d9cce6;
    --text-white: #ffffff;
  }
  * { box-sizing: border-box; margin: 0; padding: 0; }
  html, body { width: 1200px; height: 1200px; overflow: hidden; }
  body {
    background: var(--lilac-bg);
    position: relative;
    font-family: "Quicksand", sans-serif;
  }
  .card {
    position: absolute;
    left: 250px;
    width: 700px;
    height: 400px;
    border-radius: 18px;
    overflow: hidden;
    box-shadow: 0 10px 28px rgba(90, 60, 120, 0.18);
  }
  .card--front { top: 160px; background: var(--card-purple); }
  .card--back  { top: 640px; background: var(--card-white); }

  .front__title {
    position: absolute;
    left: 0; right: 0;
    top: 162px;
    text-align: center;
    font-family: "Cormorant Garamond", serif;
    font-weight: 600;
    font-size: 33px;
    letter-spacing: 4px;
    color: var(--text-white);
  }
  .front__tagline-row {
    position: absolute;
    left: 110px;
    right: 110px;
    top: 216px;
    display: flex;
    align-items: center;
    gap: 20px;
  }
  .front__rule {
    flex: 1;
    height: 1px;
    background: var(--rule-light);
  }
  .front__tagline {
    font-size: 15px;
    letter-spacing: 2.2px;
    color: var(--text-white);
    white-space: nowrap;
  }

  .back__pattern {
    position: absolute;
    left: 0; top: 0; bottom: 0;
    width: 85px;
    background: linear-gradient(180deg, #9a7fbb, #a68cc4 50%, #9a7fbb);
  }
  .back__title {
    position: absolute;
    left: 85px; right: 0;
    top: 68px;
    text-align: center;
    font-family: "Cormorant Garamond", serif;
    font-weight: 600;
    font-size: 34px;
    letter-spacing: 3.5px;
    color: var(--ink-purple);
  }
  .back__subtitle {
    position: absolute;
    left: 85px; right: 0;
    top: 116px;
    text-align: center;
    font-family: "Cormorant Garamond", serif;
    font-weight: 600;
    font-size: 16px;
    letter-spacing: 3.5px;
    color: var(--ink-purple);
  }
  .contact {
    position: absolute;
    left: 135px;
    display: flex;
    align-items: flex-start;
    gap: 18px;
    color: var(--ink-purple);
  }
  .contact__icon { flex: none; width: 36px; height: 36px; }
  .contact__text { font-size: 20px; line-height: 27px; padding-top: 4px; }
  .contact--phone { top: 186px; }
  .contact--phone .contact__text { font-size: 26px; padding-top: 1px; }
  .contact--address { top: 238px; }
  .contact--email { top: 306px; }
</style>
</head>
<body>

  <section class="card card--front" aria-label="Business card front">
    <h1 class="front__title">DARNELL'S SHOE STORE</h1>
    <div class="front__tagline-row">
      <span class="front__rule"></span>
      <span class="front__tagline">Family Owned Since 1947</span>
    </div>
  </section>

  <section class="card card--back" aria-label="Business card back">
    <div class="back__pattern" role="img" aria-label="Decorative band of flowing wave lines in lilac on purple"></div>
    <h2 class="back__title">DARNELL'S SHOE STORE</h2>
    <p class="back__subtitle">FOOTWEAR FITTING SPECIALIST</p>

    <div class="contact contact--phone">
      <svg class="contact__icon" viewBox="0 0 36 36" aria-hidden="true">
        <circle cx="18" cy="18" r="18" fill="var(--icon-purple)"/>
        <path d="M12.5 10.5c1-.6 2-.3 2.5.6l1.3 2.4c.4.8.2 1.6-.5 2.1l-1 .7c.8 1.9 2.3 3.4 4.2 4.3l.7-1c.5-.7 1.4-.9 2.1-.5l2.4 1.3c.9.5 1.2 1.5.6 2.5-1 1.7-2.6 2.5-4.4 1.9-4.6-1.5-8.2-5.1-9.7-9.7-.6-1.8.2-3.4 1.8-4.6z" fill="#fff"/>
        <path d="M20 10.5a5.5 5.5 0 0 1 5.5 5.5M20 13.2a2.8 2.8 0 0 1 2.8 2.8" stroke="#fff" stroke-width="1.3" fill="none" stroke-linecap="round"/>
      </svg>
      <span class="contact__text">9187 2630</span>
    </div>

    <div class="contact contact--address">
      <svg class="contact__icon" viewBox="0 0 36 36" aria-hidden="true">
        <circle cx="18" cy="18" r="18" fill="var(--icon-purple)"/>
        <path d="M18 8.5a6 6 0 0 0-6 6c0 4.5 6 11.5 6 11.5s6-7 6-11.5a6 6 0 0 0-6-6z" fill="#fff"/>
        <circle cx="18" cy="14.5" r="2.2" fill="var(--icon-purple)"/>
      </svg>
      <span class="contact__text">218 Quarry St, Fernleigh Downs 3187<br>(cnr. Hartwick Rd and Quarry St)</span>
    </div>

    <div class="contact contact--email">
      <svg class="contact__icon" viewBox="0 0 36 36" aria-hidden="true">
        <circle cx="18" cy="18" r="18" fill="var(--icon-purple)"/>
        <rect x="9.5" y="12" width="17" height="12" rx="1" fill="#fff"/>
        <path d="M10 12.8l8 6 8-6M10 23.3l5.6-5M26 23.3l-5.6-5" stroke="var(--icon-purple)" stroke-width="1.1" fill="none"/>
      </svg>
      <span class="contact__text">darnellshoes218@examplemail.com</span>
    </div>
  </section>

</body>
</html>
```